Business Card Design

Looking for business card designs for a new business. there will be two cards of the same design (both lots of information below in contact info). We would like the logo diagonally across the card with the information split above and below the logo similar to sketch. happy to look at similar alternatives
Please use same colours as in logo design

Industry/Entity Type

Business

Contact Information for Business Card

Gareth Mullins
mob - 0498 172 309
ph - 02 4839 2100
fax - 02 4839 2400
email - gaz@ridgelinetrusses.com.au
14 Calloway Road, Parrinda NSW 2340

Desmond Alcott
mob - 0426 918 753
ph - 02 4839 2100
fax - 02 4839 2400
email - desmond@ridgelinetrusses.com.au

```html
<!DOCTYPE html>
<html lang="en">
<head>
<meta charset="utf-8">
<title>Ridgeline Trusses – Business Card</title>
<link href="https://fonts.googleapis.com/css2?family=Source+Sans+3:wght@400;600;700&display=swap" rel="stylesheet">
<style>
  :root {
    --teal: #0e7f7e;
    --white: #ffffff;
    --ink: #111314;
    --stage-light: #575757;
    --stage-dark: #262626;
  }
  html, body {
    margin: 0;
    padding: 0;
    width: 1200px;
    height: 999px;
    overflow: hidden;
  }
  body {
    position: relative;
    background: radial-gradient(ellipse at 50% 50%, var(--stage-light) 0%, #444 55%, var(--stage-dark) 100%);
    font-family: "Source Sans 3", "Myriad Pro", Arial, sans-serif;
  }
  .card {
    position: absolute;
    left: 75px;
    top: 199px;
    width: 1050px;
    height: 600px;
    background: var(--teal);
    overflow: hidden;
  }
  .card-band {
    position: absolute;
    inset: 0;
  }
  .holder-name {
    position: absolute;
    left: 40px;
    top: 36px;
    margin: 0;
    font-size: 41px;
    font-weight: 600;
    color: var(--white);
    letter-spacing: 0.2px;
  }
  .wordmark {
    position: absolute;
    left: 460px;
    top: 270px;
    width: 0;
    height: 0;
  }
  .wordmark-text {
    position: absolute;
    left: 0;
    top: 0;
    transform: translate(-50%, -50%) rotate(-45deg);
    white-space: nowrap;
    font-size: 66px;
    font-weight: 700;
    color: var(--ink);
    letter-spacing: 0.5px;
  }
  .address {
    position: absolute;
    right: 56px;
    top: 298px;
    margin: 0;
    text-align: right;
    font-style: normal;
    font-size: 25px;
    line-height: 35px;
    color: var(--white);
  }
  .contacts {
    position: absolute;
    right: 54px;
    top: 428px;
    margin: 0;
    padding: 0;
    list-style: none;
  }
  .contact {
    display: flex;
    align-items: center;
    justify-content: flex-end;
    height: 35.5px;
    font-size: 25px;
    color: var(--white);
  }
  .contact-divider {
    display: inline-block;
    width: 2px;
    height: 24px;
    background: var(--white);
    margin: 6px 14px 0 16px;
  }
  .contact-icon {
    width: 24px;
    height: 24px;
    display: block;
  }
</style>
</head>
<body>
  <section class="card" aria-label="Business card">
    <svg class="card-band" width="1050" height="600" viewBox="0 0 1050 600" aria-hidden="true">
      <polygon points="473,0 965,0 365,600 0,600 0,473" fill="var(--white)"/>
    </svg>

    <h1 class="holder-name">Gareth Mullins</h1>

    <div class="wordmark">
      <span class="wordmark-text">Ridgeline Trusses</span>
    </div>

    <address class="address">
      14 Calloway Road,<br>
      Parrinda NSW 2340<br>
      Desmond
    </address>

    <ul class="contacts">
      <li class="contact">
        <span>0498 172 309</span><span class="contact-divider"></span>
        <svg class="contact-icon" viewBox="0 0 24 24" aria-label="Mobile">
          <rect x="2" y="1" width="20" height="22" rx="4" fill="var(--white)"/>
          <rect x="6" y="4" width="12" height="14" fill="var(--teal)"/>
          <circle cx="12" cy="20.5" r="1.2" fill="var(--teal)"/>
        </svg>
      </li>
      <li class="contact">
        <span>02 4839 2100</span><span class="contact-divider"></span>
        <svg class="contact-icon" viewBox="0 0 24 24" aria-label="Phone">
          <rect x="2" y="1" width="20" height="22" rx="4" fill="var(--white)"/>
          <path d="M14 5 l2 0 l0 4 l-2 0 c-1 2 -1 4 0 6 l2 0 l0 4 l-2 0 c-4 -3 -4 -11 0 -14z" fill="var(--teal)"/>
        </svg>
      </li>
      <li class="contact">
        <span>02 4839 2400</span><span class="contact-divider"></span>
        <svg class="contact-icon" viewBox="0 0 24 24" aria-label="Fax">
          <rect x="7" y="1" width="10" height="9" fill="var(--white)"/>
          <rect x="2" y="11" width="20" height="8" rx="1" fill="var(--white)"/>
          <rect x="2" y="20" width="20" height="3" fill="var(--white)"/>
        </svg>
      </li>
      <li class="contact">
        <span>gaz@ridgelinetrusses.com.au</span><span class="contact-divider"></span>
        <svg class="contact-icon" viewBox="0 0 24 24" aria-label="Email">
          <rect x="1" y="4" width="22" height="17" rx="4" fill="var(--white)"/>
          <path d="M3 10 L12 16 L21 10" stroke="var(--teal)" stroke-width="2" fill="none"/>
          <path d="M8 8 L12 5 L16 8" stroke="var(--teal)" stroke-width="1.6" fill="none"/>
        </svg>
      </li>
    </ul>
  </section>
</body>
</html>
```